Design flat ui arx 3 inspired app

Know how you fit in the family and how you relate as a family through a shared Tree.
· Keep track of your family as it expands
· Merge family trees or join a common family Tree
· Share family moments by uploading pictures and videos on your calendar
· Get notifications of all events, additions, and other changes to the family tree
· Know where everyone is by keeping in touch through real-time chats
· Share your Tree with friends on social media
· Search for long lost family members and friends
· A great way for your kids to know where they come from

Providing a mobile app that allows users to not only create their family trees but allow them to invite other family members to participate in the completion of the family tree. • User downloads and installs the mobile app, then they proceed to signing up • Signing up the user should provide the following information; profile picture, first name, last name, date of birth, gender, password, email address, country, current city, mobile number • The next step is verifying the mobile number by asking the user to enter the six digit number that was sent to them via sms • Once the mobile number is verified your next step is to enter your family, start with you parents, then spouse(s) or partner(s), then siblings and children if any. This step should be optional, meaning users can skip this step • The app should have a menu bar at the bottom(action bar) with fiver menu items namely, Home, Edit, Tree, Stats, Calendar. • After the user has been signed in their first experience is the home screen, with the profile picture displayed, along with the user’s first name, last name, and age(all the above should be static). Just below all this are three tabs for notifications, photos, and birthdays. • The notifications tab will list all notifications one after the other in text form, example; Kevin updated his high school, Nora added a new member, Brenda has a graduation party coming up, Gordon updated his work experience, Hilda updated her maiden name, Esther updated her siblings, Milton updated his children etc. • Photo’s tab will list all pictures uploaded sorted by latest pictures uploaded and tagged in. One should be able to scroll through the pictures and then when they click on one they can slide though them one after the next viewing them. One should be able to go back to the home screen by clicking the back button. There should be an option to add more photos and share the current ones. • The last tab should be birthdays, which simply lists all birthdays of people who have been entered into the tree from parents to spouses to siblings to children. The birthdays should be listed sorted by month then day, and you should be able to see how old the person is turning. • The next menu bar is the Edit menu which has three tabs namely personal details, family and advanced details. Personal details will have the profile picture, first name, second name, last name, date of birth, gender, twin(if twin then state), relationship status(list spouse if not single), city or place of birth, and living or not. The next tab is the family tab which list and allows you to edit parents, spouse, siblings, and children. The last tab is advanced details, which is hobbies, languages, education, and work experience. • Then the most important part of the app is the Tree function which displays the users family tree, this is all the people added so far and each person is represented by a square with smooth edges, first name and last name displayed first, then age with a green button showing online and a red one showing offline, and below a profile picture. All the relations showed by a line joining the related people. If the person has many spouses they should be stacked together and kids don’t have to show which parent us theirs. One should be able to edit a profile, view a profile, view stats, invite and share. When you invite that person an sms should be generated and the user can enter the mobile number of the family member and once the family members accepts the invitation they then are a member of the tree who can receive notifications on any changes on the tree. Anyone should be able to invite anyone and everyone should see all notifications from everyone who is a member. • The next menu is the statistics menu which displays gender stats, age distribution, birthdays, relationship status, zodiac signs, living vs not living • The last one is the calendar menu which has a calendar where people can add events, upload media, and when a day is clicked and has events on, they should show at the bottom one after the other.

```html
<!DOCTYPE html>
<html lang="en">
<head>
<meta charset="utf-8">
<title>Kinroot – family tree app screens</title>
<link rel="stylesheet" href="https://fonts.googleapis.com/css2?family=Source+Sans+3:wght@400;600;700&display=swap">
<style>
:root{
  --bg:#283340;
  --green:#80dc4c;
  --green-bar:#5db92b;
  --green-text:#67bd36;
  --green-deep:#4ea623;
  --field:#efefea;
  --field-line:#dcdcd4;
  --ink:#3a3a3a;
  --muted:#8b8b86;
  --band:#3b3e3a;
  --white:#ffffff;
  --nav:#f4f4f2;
  --teal:#17a6a8;
  --blue:#1f8fcf;
  --orange:#f4a31e;
  --avatar:#b9aba0;
}
*{box-sizing:border-box;margin:0;padding:0}
html,body{width:759px;height:1200px;overflow:hidden;background:var(--bg)}
body{font-family:"Source Sans 3",sans-serif;color:var(--ink)}
.board{position:relative;width:885px;height:1400px;transform:scale(.8576);transform-origin:0 0}
.screen{position:absolute;width:202px;overflow:hidden;background:var(--white)}
svg.icon{display:block;fill:none;stroke:currentColor;stroke-width:2;stroke-linecap:round;stroke-linejoin:round}

/* status + app bar */
.status{height:16px;display:flex;align-items:center;justify-content:space-between;padding:0 7px;font-size:8px;color:var(--white);background:var(--green-bar)}
.status .carrier{display:flex;align-items:center;gap:4px}
.status .battery{display:flex;align-items:center;gap:3px}
.status .cell{width:16px;height:4px;background:radial-gradient(circle,#fff 1.6px,transparent 1.8px) 0 0/3.3px 4px}
.status .batt{width:16px;height:7px;border:1px solid #fff;border-radius:1px;position:relative}
.status .batt::after{content:"";position:absolute;left:1px;top:1px;width:3px;height:3px;background:#fff}
.status.clear{background:rgba(0,0,0,.35)}
.appbar{height:36px;background:var(--green);display:flex;align-items:center;padding:0 9px;color:var(--white)}
.appbar .title{flex:1;text-align:center;font-size:13px;font-weight:700}
.appbar .tools{display:flex;gap:8px;margin-left:auto}

/* form parts */
.label{font-size:8px;font-weight:700;color:var(--ink);letter-spacing:.1px}
.field{height:18px;border-radius:9px;background:var(--field);border:1px solid var(--field-line);font-size:7px;color:var(--muted);display:flex;align-items:center;padding-left:10px;position:relative}
.field.select::after{content:"";position:absolute;right:8px;top:7px;border:3px solid transparent;border-top:3px solid var(--green-text)}
.row{display:flex;gap:5px}
.row .field{flex:1}
.btn{height:27px;border-radius:14px;background:var(--green);color:#2f5a14;font-size:11px;display:flex;align-items:center;justify-content:center;font-weight:600}

/* photo placeholders */
.photo-bg{position:absolute;inset:0;background:linear-gradient(160deg,#6a5a4e,#9a7c66 35%,#5c4c42 65%,#3a3532)}
.portrait{height:92px;background:linear-gradient(90deg,#e6e6e4 0%,#dadad7 45%,#6b5446 62%,#3f342e 78%,#e4e4e1 100%)}

/* tabs band */
.band{background:var(--band);height:41px;display:flex;align-items:center;padding:0 10px}
.tabs{flex:1;display:flex;height:18px;border-radius:9px;background:var(--field);overflow:hidden;font-size:8px;font-weight:600;color:var(--ink)}
.tabs span{flex:1;display:flex;align-items:center;justify-content:center;border-right:1px solid var(--field-line)}
.tabs span.on{background:var(--green);color:var(--white);border:none}
.month-pill{height:18px;border-radius:9px;background:var(--field);border:1px solid var(--field-line);font-size:8px;font-weight:700;display:flex;align-items:center;justify-content:center}

/* bottom nav */
.navbar{position:absolute;left:0;right:0;bottom:0;height:29px;background:var(--nav);border-top:1px solid #e3e3df;display:flex}
.navbar a{flex:1;display:flex;flex-direction:column;align-items:center;justify-content:center;gap:2px;font-size:6.5px;color:#6a6a66;text-decoration:none}
.navbar a.on{color:var(--green-text)}
.navbar svg{width:10px;height:10px}

/* brand */
.brand{display:flex;flex-direction:column;align-items:center;gap:6px;color:var(--green)}
.brand .dot{border-radius:50%;background:var(--green)}
.brand .name{font-weight:700;color:var(--green)}

/* family section */
.family-section{padding:10px 11px 0;height:179px;border-bottom:1px solid #ececec}
.family-section h3{font-size:10px;color:var(--green-text);text-align:center;position:relative;margin:1px 0 5px;font-weight:700;letter-spacing:.3px}
.family-section h3 .add{position:absolute;right:-2px;top:-2px;font-size:14px;font-weight:400}
.family-section .field{margin-bottom:5px}
.toggle{height:18px;border-radius:9px;border:1px solid var(--field-line);background:var(--field);display:flex;overflow:hidden;flex:0 0 60px}
.toggle span{flex:1;display:flex;align-items:center;justify-content:center;font-size:9px;font-weight:700;color:var(--muted)}
.toggle span.on{background:var(--green);color:var(--white);border-radius:9px}
.dots{display:flex;justify-content:center;gap:3px;margin-top:12px}
.dots i{width:8px;height:8px;border-radius:50%;background:#ececec}
.dots i.on{background:var(--green)}

/* list */
.person{height:33.5px;display:flex;align-items:center;border-bottom:1px solid #ececec;font-size:11px;color:var(--green-text)}
.person .num{width:24px;height:100%;display:flex;align-items:center;justify-content:center;background:#f3f3f1;color:var(--ink);font-size:8px}
.avatar{border-radius:50%;background:var(--avatar);flex:none}
.person .avatar{width:20px;height:20px;margin:0 9px 0 8px}
.person .name{flex:1}
.person .go{width:16px;height:16px;border-radius:50%;border:1.5px solid var(--green);margin-right:9px;display:flex;align-items:center;justify-content:center;color:var(--green)}
.person.on{background:var(--green);color:var(--white)}
.person.on .num{background:var(--green-deep);color:var(--white)}
.person.on .go{border-color:#fff;color:#fff}

/* birthday rows */
.bday{height:30.5px;display:flex;align-items:center;border-bottom:1px solid #ececec;font-size:8px;padding-left:9px}
.bday .d{width:14px}
.bday .box{width:16px;height:16px;border:1px solid #d5d5d0;background:#f2f2ef;font-size:7px;display:flex;align-items:center;justify-content:center;margin-right:6px}
.bday .who{width:66px}
.month-grid{display:grid;grid-template-columns:repeat(3,57px);column-gap:6px;padding:10px 10px 0}
.month-grid .names{font-size:7.5px;text-align:center;line-height:16px;color:var(--ink);margin:3px 0 6px;min-height:48px}
</style>
</head>
<body>
<svg width="0" height="0" style="position:absolute" aria-hidden="true">
  <defs>
    <symbol id="i-menu" viewBox="0 0 12 12"><path d="M1 2.5h10M1 6h10M1 9.5h10"/></symbol>
    <symbol id="i-search" viewBox="0 0 12 12"><circle cx="5" cy="5" r="3.4"/><path d="M7.6 7.6l3 3" stroke-width="2.4"/></symbol>
    <symbol id="i-list" viewBox="0 0 12 12"><path d="M1 2h1.5M1 6h1.5M1 10h1.5M4.5 2H11M4.5 6H11M4.5 10H11" stroke-width="1.5"/></symbol>
    <symbol id="i-share" viewBox="0 0 12 12"><circle cx="9" cy="2.5" r="1.6" fill="currentColor"/><circle cx="3" cy="6" r="1.6" fill="currentColor"/><circle cx="9" cy="9.5" r="1.6" fill="currentColor"/><path d="M9 2.5L3 6l6 3.5" stroke-width="1.4"/></symbol>
    <symbol id="i-home" viewBox="0 0 12 12"><path d="M1 6L6 1.5 11 6M2.5 5v6h7V5" fill="currentColor" stroke-width="1"/></symbol>
    <symbol id="i-edit" viewBox="0 0 12 12"><path d="M2 10l1-3 6-6 2 2-6 6z" fill="currentColor" stroke-width="1"/></symbol>
    <symbol id="i-tree" viewBox="0 0 12 12"><rect x="4" y="0.8" width="4" height="3" rx=".5" fill="currentColor" stroke="none"/><rect x="0.8" y="8.2" width="4" height="3" rx=".5" fill="currentColor" stroke="none"/><rect x="7.2" y="8.2" width="4" height="3" rx=".5" fill="currentColor" stroke="none"/><path d="M6 3.8v2.3M2.8 8.2V6.1h6.4v2.1" stroke-width="1.1"/></symbol>
    <symbol id="i-cal" viewBox="0 0 12 12"><rect x="1.5" y="2.5" width="9" height="8" rx="1" stroke-width="1.3"/><path d="M1.5 5h9M4 1v2.5M8 1v2.5" stroke-width="1.3"/></symbol>
    <symbol id="i-stats" viewBox="0 0 12 12"><path d="M2 11V6M5 11V2M8 11V4.5M11 11V7" stroke-width="2" stroke-linecap="butt"/></symbol>
    <symbol id="i-next" viewBox="0 0 12 12"><path d="M5 3.5L7.5 6 5 8.5" stroke-width="1.8"/></symbol>
    <symbol id="i-back" viewBox="0 0 12 12"><path d="M8 1.5L3.5 6 8 10.5" stroke-width="1.8"/></symbol>
  </defs>
</svg>

<main class="board">

  <!-- Splash -->
  <section class="screen splash" style="left:63px;top:35px;height:303px">
    <div class="photo-bg" role="img" aria-label="Blurred family photograph in warm brown tones"></div>
    <div class="status clear" style="position:relative"><span class="carrier"><i class="cell"></i>Telvo</span><span>4:21PM</span><span class="battery">20%<i class="batt"></i></span></div>
    <div class="brand" style="position:absolute;left:0;right:0;top:90px">
      <i class="dot" style="width:34px;height:34px"></i>
      <span class="name" style="font-size:26px">Kinroot</span>
    </div>
    <svg style="position:absolute;left:80px;top:227px" width="42" height="42" viewBox="0 0 42 42" aria-label="Loading 33 percent">
      <circle cx="21" cy="21" r="17" fill="none" stroke="#fff" stroke-width="6" stroke-dasharray="5 1.6"/>
      <circle cx="21" cy="21" r="17" fill="none" stroke="var(--green)" stroke-width="6" stroke-dasharray="35 72" transform="rotate(-90 21 21)"/>
      <circle cx="21" cy="21" r="13" fill="#3d3a36"/>
      <text x="21" y="24.5" text-anchor="middle" font-size="9" font-weight="700" fill="#fff" font-family="Source Sans 3, sans-serif">33%</text>
    </svg>
  </section>

  <!-- Login -->
  <section class="screen login" style="left:308px;top:35px;height:353px">
    <div class="photo-bg" role="img" aria-label="Blurred family photograph in warm brown tones"></div>
    <div class="status clear" style="position:relative"><span class="carrier"><i class="cell"></i>Telvo</span><span>4:21PM</span><span class="battery">20%<i class="batt"></i></span></div>
    <div style="position:absolute;left:14px;top:28px;width:174px;height:311px;background:#fff;border-radius:10px;padding:0 14px">
      <div class="brand" style="margin-top:28px">
        <i class="dot" style="width:22px;height:22px"></i>
        <span class="name" style="font-size:17px">Kinroot</span>
      </div>
      <div class="label" style="margin-top:33px">MOBILE NUMBER</div>
      <div class="field" style="margin-top:4px"></div>
      <div class="label" style="margin-top:10px">PASSWORD</div>
      <div class="field" style="margin-top:4px"></div>
      <div class="btn" style="margin-top:17px">LOGIN</div>
      <div style="text-align:center;font-size:8px;margin-top:16px">REGISTER</div>
      <div style="position:relative;height:14px;margin:5px 22px 0;display:flex;align-items:center;justify-content:center">
        <i style="position:absolute;left:0;right:0;top:7px;height:1px;background:#cfcfca"></i>
        <span style="position:relative;width:14px;height:14px;border-radius:50%;background:var(--green);font-size:7px;display:flex;align-items:center;justify-content:center;color:#2f5a14">or</span>
      </div>
      <div style="text-align:center;font-size:8px;margin-top:6px">FORGOT PASSWORD?</div>
    </div>
  </section>

  <!-- New registration -->
  <section class="screen register" style="left:551px;top:35px;height:530px;background:var(--band)">
    <div class="status"><span class="carrier"><i class="cell"></i>Telvo</span><span>4:21PM</span><span class="battery">20%<i class="batt"></i></span></div>
    <header class="appbar"><svg class="icon" width="12" height="12"><use href="#i-menu"/></svg><span class="title">New Registration</span><svg class="icon" width="12" height="12"><use href="#i-search"/></svg></header>
    <form style="margin:16px 14px 0;background:#fff;border-radius:8px;height:447px;padding:10px 14px 0;display:flex;flex-direction:column">
      <div class="label">PROFILE PICTURE</div>
      <div class="field" style="margin:3px 0 9px;padding:0;justify-content:flex-end"><span style="height:18px;width:50px;margin:-1px -1px 0 0;border-radius:9px;background:var(--green);color:#fff;font-size:7px;display:flex;align-items:center;justify-content:center">BROWS</span></div>
      <div class="label">FIRST NAME</div><div class="field" style="margin:3px 0 9px">JOHN</div>
      <div class="label">LAST NAME</div><div class="field" style="margin:3px 0 9px">SMITH</div>
      <div class="label">DATE OF BIRTH</div>
      <div class="row" style="margin:3px 0 9px"><div class="field select">1</div><div class="field select">JAN</div><div class="field select">1985</div></div>
      <div class="label">GENDER</div><div class="field select" style="margin:3px 0 9px">MALE</div>
      <div class="label">PASSWORD</div><div class="field" style="margin:3px 0 9px">**********</div>
      <div class="label">EMAIL ADDRESS</div><div class="field" style="margin:3px 0 9px">AB@EXAMPLE.COM</div>
      <div class="label">COUNTRY</div><div class="field select" style="margin:3px 0 9px">INDIA</div>
      <div class="label">CURRENT CITY</div><div class="field" style="margin:3px 0 9px">NEW DELHI</div>
      <div class="label">MOBILE NUMBER</div><div class="field" style="margin:3px 0 0">+91-912345XXXX</div>
      <div class="btn" style="margin-top:13px">REGISTER NOW</div>
    </form>
  </section>

  <!-- Add family -->
  <section class="screen add-family" style="left:63px;top:374px;height:806px">
    <div class="status"><span class="carrier"><i class="cell"></i>Telvo</span><span>4:21PM</span><span class="battery">20%<i class="batt"></i></span></div>
    <header class="appbar"><svg class="icon" width="12" height="12"><use href="#i-menu"/></svg><span class="title">Add Family</span><svg class="icon" width="12" height="12"><use href="#i-search"/></svg></header>
    <div class="band" style="height:41px"><div class="tabs"><span style="border:none"></span><span class="on">Family</span><span style="border:none"></span></div></div>

    <div class="family-section">
      <h3>PARENTS<span class="add">+</span></h3>
      <div class="field"></div><div class="field"></div>
      <div class="label" style="margin-top:6px">DATE OF BIRTH</div>
      <div class="row" style="margin-top:4px"><div class="field select">1</div><div class="field select">JAN</div><div class="field select">1985</div></div>
      <div class="row label" style="margin-top:1px"><span style="flex:1">GENDER</span><span style="flex:0 0 60px">ALIVE</span></div>
      <div class="row" style="margin-top:4px"><div class="field select">MALE</div><div class="toggle"><span class="on">X</span><span>✓</span></div></div>
      <div class="dots"><i class="on"></i><i></i><i></i></div>
    </div>
    <div class="family-section">
      <h3>SPOUSES<span class="add">+</span></h3>
      <div class="field"></div><div class="field"></div>
      <div class="label" style="margin-top:6px">DATE OF BIRTH</div>
      <div class="row" style="margin-top:4px"><div class="field select">1</div><div class="field select">JAN</div><div class="field select">1985</div></div>
      <div class="row label" style="margin-top:1px"><span style="flex:1">GENDER</span><span style="flex:0 0 60px">ALIVE</span></div>
      <div class="row" style="margin-top:4px"><div class="field select">MALE</div><div class="toggle"><span class="on">X</span><span>✓</span></div></div>
      <div class="dots"><i class="on"></i><i></i><i></i></div>
    </div>
    <div class="family-section">
      <h3>SHIBLINGS<span class="add">+</span></h3>
      <div class="field"></div><div class="field"></div>
      <div class="label" style="margin-top:6px">DATE OF BIRTH</div>
      <div class="row" style="margin-top:4px"><div class="field select">1</div><div class="field select">JAN</div><div class="field select">1985</div></div>
      <div class="row label" style="margin-top:1px"><span style="flex:1">GENDER</span><span style="flex:0 0 60px">ALIVE</span></div>
      <div class="row" style="margin-top:4px"><div class="field select">MALE</div><div class="toggle"><span class="on">X</span><span>✓</span></div></div>
      <div class="dots"><i class="on"></i><i></i><i></i></div>
    </div>
    <div class="family-section" style="border:none">
      <h3>CHILDREN<span class="add">+</span></h3>
      <div class="field"></div><div class="field"></div>
      <div class="label" style="margin-top:6px">DATE OF BIRTH</div>
      <div class="row" style="margin-top:4px"><div class="field select">1</div><div class="field select">JAN</div><div class="field select">1985</div></div>
      <div class="row label" style="margin-top:1px"><span style="flex:1">GENDER</span><span style="flex:0 0 60px">ALIVE</span></div>
      <div class="row" style="margin-top:4px"><div class="field select">MALE</div><div class="toggle"><span class="on">X</span><span>✓</span></div></div>
      <div class="dots"><i class="on"></i><i></i><i></i></div>
    </div>
  </section>

  <!-- Profile: birthdays by month -->
  <section class="screen profile-birthdays" style="left:308px;top:415px;height:320px">
    <div class="status"><span class="carrier"><i class="cell"></i>Telvo</span><span>4:21PM</span><span class="battery">20%<i class="batt"></i></span></div>
    <header class="appbar"><svg class="icon" width="12" height="12"><use href="#i-menu"/></svg><span class="title">Kevin Hale</span><svg class="icon" width="12" height="12"><use href="#i-search"/></svg></header>
    <div class="portrait" role="img" aria-label="Profile portrait photo of the user"></div>
    <div class="band"><div class="tabs"><span>Notifications</span><span>Photos</span><span class="on">Birthdays</span></div></div>
    <div style="height:41px;display:flex;align-items:center;padding-left:9px;gap:8px;border-bottom:1px solid #ececec;background:#fafaf8">
      <svg class="icon" width="11" height="11" style="color:var(--green)"><use href="#i-back"/></svg>
      <span class="month-pill" style="width:56px">January</span>
    </div>
    <div class="bday"><span class="d">9</span><span class="box">8</span><span class="who">Jan Doe</span><span>31 Years</span></div>
    <div class="bday"><span class="d">18</span><span class="box"></span><span class="who">Jan Doe</span><span>31 Years</span></div>
    <div class="bday" style="border:none"><span class="d">31</span><span class="box"></span><span class="who">Jan Doe</span><span>31 Years</span></div>
  </section>

  <!-- Tree list -->
  <section class="screen tree-list" style="left:308px;top:766px;height:383px">
    <div class="status"><span class="carrier"><i class="cell"></i>Telvo</span><span>4:21PM</span><span class="battery">20%<i class="batt"></i></span></div>
    <header class="appbar"><svg class="icon" width="12" height="12"><use href="#i-menu"/></svg><span class="tools"><svg class="icon" width="12" height="12"><use href="#i-list"/></svg><svg class="icon" width="12" height="12"><use href="#i-share"/></svg><svg class="icon" width="12" height="12"><use href="#i-search"/></svg></span></header>
    <ol style="list-style:none">
      <li class="person"><span class="num">1</span><i class="avatar"></i><span class="name">Kevin Hale</span><span class="go"><svg class="icon" width="9" height="9"><use href="#i-next"/></svg></span></li>
      <li class="person"><span class="num">2</span><i class="avatar"></i><span class="name">Kevin Hale</span><span class="go"><svg class="icon" width="9" height="9"><use href="#i-next"/></svg></span></li>
      <li class="person"><span class="num">3</span><i class="avatar"></i><span class="name">Kevin Hale</span><span class="go"><svg class="icon" width="9" height="9"><use href="#i-next"/></svg></span></li>
      <li class="person on"><span class="num">4</span><i class="avatar"></i><span class="name">Kevin Hale</span><span class="go"><svg class="icon" width="9" height="9"><use href="#i-next"/></svg></span></li>
      <li class="person"><span class="num">5</span><i class="avatar"></i><span class="name">Kevin Hale</span><span class="go"><svg class="icon" width="9" height="9"><use href="#i-next"/></svg></span></li>
      <li class="person"><span class="num">6</span><i class="avatar"></i><span class="name">Kevin Hale</span><span class="go"><svg class="icon" width="9" height="9"><use href="#i-next"/></svg></span></li>
      <li class="person"><span class="num">7</span><i class="avatar"></i><span class="name">Kevin Hale</span><span class="go"><svg class="icon" width="9" height="9"><use href="#i-next"/></svg></span></li>
      <li class="person"><span class="num">8</span><i class="avatar"></i><span class="name">Kevin Hale</span><span class="go"><svg class="icon" width="9" height="9"><use href="#i-next"/></svg></span></li>
      <li class="person"><span class="num">9</span><i class="avatar"></i><span class="name">Kevin Hale</span><span class="go"><svg class="icon" width="9" height="9"><use href="#i-next"/></svg></span></li>
    </ol>
    <nav class="navbar">
      <a><svg class="icon"><use href="#i-home"/></svg>HOME</a>
      <a><svg class="icon"><use href="#i-edit"/></svg>EDIT</a>
      <a class="on"><svg class="icon"><use href="#i-tree"/></svg>TREE</a>
      <a><svg class="icon"><use href="#i-cal"/></svg>CALENDER</a>
      <a><svg class="icon"><use href="#i-stats"/></svg>STATS</a>
    </nav>
  </section>

  <!-- Tree circle -->
  <section class="screen tree-circle" style="left:551px;top:586px;height:379px">
    <div class="status"><span class="carrier"><i class="cell"></i>Telvo</span><span>4:21PM</span><span class="battery">20%<i class="batt"></i></span></div>
    <header class="appbar"><svg class="icon" width="12" height="12"><use href="#i-menu"/></svg><span class="tools"><svg class="icon" width="12" height="12"><use href="#i-list"/></svg><svg class="icon" width="12" height="12"><use href="#i-share"/></svg><svg class="icon" width="12" height="12"><use href="#i-search"/></svg></span></header>
    <svg width="202" height="297" viewBox="0 0 202 297" font-family="Source Sans 3, sans-serif" aria-label="Circular family tree">
      <g fill="none" stroke="#e2e2de" stroke-width="1">
        <circle cx="101" cy="137" r="87"/><circle cx="101" cy="137" r="58"/><circle cx="101" cy="137" r="32"/>
        <path d="M101 40v194M4 137h194"/>
      </g>
      <g fill="none" stroke-width="14">
        <path id="arc-teal" d="M33.3 112.4A72 72 0 0 1 70.6 71.8" stroke="var(--teal)"/>
        <path id="arc-green" d="M94.7 65.3A72 72 0 0 1 168.7 161.6" stroke="var(--green)"/>
        <path id="arc-orange" d="M94.7 208.7A72 72 0 0 0 147.3 192.2" stroke="var(--orange)"/>
        <path id="arc-blue" d="M30.1 124.5A72 72 0 0 0 70.6 202.2" stroke="var(--blue)"/>
      </g>
      <g font-size="5.5" font-weight="700" fill="#fff">
        <text dy="2"><textPath href="#arc-teal" startOffset="22%">Kevin Hale</textPath></text>
        <text dy="2"><textPath href="#arc-green" startOffset="12%">Kevin Hale</textPath></text>
        <text dy="2"><textPath href="#arc-green" startOffset="60%">Kevin Hale</textPath></text>
        <text dy="2"><textPath href="#arc-orange" startOffset="25%">Kevin Hale</textPath></text>
        <text dy="2"><textPath href="#arc-blue" startOffset="32%">Kevin Hale</textPath></text>
      </g>
      <g fill="var(--avatar)" stroke="#fff" stroke-width="1.5">
        <circle cx="72" cy="66" r="7"/><circle cx="97" cy="61" r="7"/><circle cx="173" cy="158" r="7"/>
        <circle cx="151" cy="196" r="7"/><circle cx="92" cy="213" r="7"/><circle cx="67" cy="206" r="7"/>
        <circle cx="27" cy="121" r="7"/>
        <circle cx="101" cy="137" r="23" stroke="var(--green)" stroke-width="2"/>
      </g>
      <rect x="80" y="157" width="42" height="9" fill="#e4e4e0"/>
      <text x="101" y="164" text-anchor="middle" font-size="6" fill="#555">Kevin Hale</text>
    </svg>
    <nav class="navbar">
      <a><svg class="icon"><use href="#i-home"/></svg>HOME</a>
      <a><svg class="icon"><use href="#i-edit"/></svg>EDIT</a>
      <a class="on"><svg class="icon"><use href="#i-tree"/></svg>TREE</a>
      <a><svg class="icon"><use href="#i-cal"/></svg>CALENDER</a>
      <a><svg class="icon"><use href="#i-stats"/></svg>STATS</a>
    </nav>
  </section>

  <!-- Profile: birthdays overview -->
  <section class="screen profile-months" style="left:551px;top:1003px;height:354px">
    <div class="status"><span class="carrier"><i class="cell"></i>Telvo</span><span>4:21PM</span><span class="battery">20%<i class="batt"></i></span></div>
    <header class="appbar"><svg class="icon" width="12" height="12"><use href="#i-menu"/></svg><span class="title">Kevin Hale</span><svg class="icon" width="12" height="12"><use href="#i-search"/></svg></header>
    <div class="portrait" role="img" aria-label="Profile portrait photo of the user"></div>
    <div class="band"><div class="tabs"><span>Notifications</span><span>Photos</span><span class="on">Birthdays</span></div></div>
    <div class="month-grid">
      <div><div class="month-pill">January</div><div class="names">9 Jan Doe<br>18 Jane Doe<br>21 Joe Doe</div></div>
      <div><div class="month-pill">February</div><div class="names">27 Jude Doe<br>27 Jude Doe<br>27 Jude Doe</div></div>
      <div><div class="month-pill">March</div><div class="names"></div></div>
      <div><div class="month-pill">April</div><div class="names">11 Jeff Doe<br>21 Kevin Doe<br>25 Hilda Deo</div></div>
      <div><div class="month-pill">May</div><div class="names">21 Jude Doe<br>27 Jude Doe<br>31 Jude Doe</div></div>
      <div><div class="month-pill">June</div><div class="names"></div></div>
    </div>
  </section>

</main>
</body>
</html>
```